Baseball Themed Power Point Template

I am hosting a business meeting in Chicago in July. The audience is a group of young sales professionals.

My meeting needs a generic PowerPoint presentation template with a baseball all-star theme. I have browsed templates for sale on-line and many of them are boring--they show a baseball laying in the grass. None of them have caught my eye.

I would like the template for my meeting to be fun, modern and celebratory. It will only be used once so I don't need a logo or design that needs to have any longevity. The template will be used for an activity that lasts one day only.

As for colors, I would like a red, white and blue color scheme to match the colors of the Dunmore Hawks-- but please don't violate any copyrights. I only attach it for color consideration.

My preferred orientation is 16 by 9. I need a title page, a text page, and a couple color break pages.

I have attached two files--one is the Dunmore Hawks logo so you can match colors. The other is a flyer that interested me because it seemed fun and celebratory.

Target Market(s)

Young professionals, 25-35, sales and marketing. They are fun, competitive and energetic.

Industry/Entity Type

Business

Font styles to use
Sans Serif

Colors
0255a3
ec1f27
ffffff

Requirements
Must have
• Red, white and blue colors. Energy. Modern looking.
Should not have
• Do not violate the Dunmore Hawks logo-I just want to simulate the colors.

```html
<!DOCTYPE html>
<html lang="en">
<head>
<meta charset="utf-8">
<title>Dunmore Hawks All-Star Meeting – Slide Template</title>
<link rel="stylesheet" href="https://fonts.googleapis.com/css2?family=Open+Sans:wght@400;600;700&display=swap">
<style>
  :root {
    --board: #666666;
    --navy: #0d1a6e;
    --blue: #0b1f7a;
    --red: #d9000d;
    --red-deep: #b8000a;
    --white: #ffffff;
    --ink: #333333;
    --muted: #555555;
    --agenda-bg: #f1f3f6;
  }
  * { box-sizing: border-box; margin: 0; padding: 0; }
  html, body { width: 1200px; height: 847px; overflow: hidden; }
  body {
    background: var(--board);
    font-family: "Open Sans", Arial, sans-serif;
    position: relative;
  }
  .slide {
    position: absolute;
    overflow: hidden;
    box-shadow: 3px 5px 8px rgba(0,0,0,0.45);
  }
  .photo { position: absolute; inset: 0; }
  .slogan {
    position: absolute;
    color: var(--white);
    font-weight: 700;
    font-size: 26.5px;
    line-height: 36.5px;
    text-transform: uppercase;
    letter-spacing: 0.2px;
    text-shadow: 0 1px 3px rgba(0,0,0,0.35);
  }

  /* Title slide with points band */
  .slide--points { left: 35px; top: 85px; width: 535px; height: 298px; }
  .slide--points .photo {
    bottom: 58px;
    background: linear-gradient(100deg, #c48a4f 0%, #d9a56a 30%, #8b7a4c 55%, #e6d3b0 75%, #6f5a3a 100%);
  }
  .slide--points .slogan { left: 51px; top: 63px; }
  .points { position: absolute; left: 0; right: 0; bottom: 0; height: 58px; display: flex; }
  .point {
    flex: 1; position: relative;
    display: flex; align-items: flex-end; justify-content: center;
    padding-bottom: 21px;
    font-size: 10.5px; color: var(--white);
  }
  .point--blue { background: var(--blue); }
  .point--white { background: linear-gradient(#ffffff, #e2e2e2); color: #222; }
  .point--red { background: linear-gradient(var(--red), var(--red-deep)); }
  .point svg { position: absolute; top: -9px; left: 50%; margin-left: -15px; }

  /* Title slide with date */
  .slide--title { left: 635px; top: 95px; width: 526px; height: 296px; }
  .slide--title .photo {
    background: linear-gradient(180deg, #1d2a22 0%, #2f4a2a 18%, #3f7a22 35%, #4c8f1f 60%, #2e5a14 100%);
  }
  .slide--title .slogan { left: 38px; top: 32px; }
  .date {
    position: absolute; left: 46px; top: 178px;
    color: var(--white); font-weight: 700; font-size: 12.5px;
  }

  /* Agenda slide */
  .slide--agenda { left: 303px; top: 462px; width: 567px; height: 318px; background: var(--agenda-bg); }
  .slide--agenda .photo {
    background: linear-gradient(180deg, #f6f7f9 0%, #eef1f1 40%, #e4ebe0 70%, #dde5d6 100%);
  }
  .agenda-head {
    position: absolute; left: 43px; top: 28px;
    border-left: 3px solid var(--blue);
    padding-left: 8px; height: 36px;
  }
  .agenda-head h1 { font-size: 16.5px; font-weight: 600; color: var(--navy); line-height: 19px; }
  .agenda-head p { font-size: 11px; color: var(--red); line-height: 15px; }
  .agenda-item { position: absolute; width: 225px; }
  .agenda-item svg { position: absolute; left: -18px; top: 3px; }
  .agenda-item h2 { font-size: 13.5px; font-weight: 700; color: var(--navy); line-height: 17px; }
  .agenda-item p { font-size: 8.5px; color: var(--muted); line-height: 12px; }
</style>
</head>
<body>

  <section class="slide slide--points">
    <div class="photo" role="img" aria-label="Photo of a baseball resting in a leather glove beside a wooden bat on grass"></div>
    <h1 class="slogan">Your presentation<br>slogan comes here<br>explain some words</h1>
    <div class="points">
      <div class="point point--blue">
        <svg width="30" height="30" viewBox="0 0 30 30"><circle cx="15" cy="15" r="13" fill="none" stroke="var(--red)" stroke-width="2.5"/><path d="M12 9l7 6-7 6" fill="none" stroke="var(--blue)" stroke-width="2.5"/></svg>
        Insert your Points here
      </div>
      <div class="point point--white">
        <svg width="30" height="30" viewBox="0 0 30 30"><circle cx="15" cy="15" r="13" fill="none" stroke="var(--blue)" stroke-width="2.5"/><path d="M12 9l7 6-7 6" fill="none" stroke="var(--blue)" stroke-width="2.5"/></svg>
        Insert your Points here
      </div>
      <div class="point point--red">
        <svg width="30" height="30" viewBox="0 0 30 30"><circle cx="15" cy="15" r="13" fill="none" stroke="var(--white)" stroke-width="2.5"/><path d="M12 9l7 6-7 6" fill="none" stroke="var(--white)" stroke-width="2.5"/></svg>
        Insert your Points here
      </div>
    </div>
  </section>

  <section class="slide slide--title">
    <div class="photo" role="img" aria-label="Photo of a baseball, glove and bat lying in the outfield grass"></div>
    <h1 class="slogan">Your presentation<br>slogan comes<br>here explain some<br>words</h1>
    <p class="date">June 2016</p>
  </section>

  <section class="slide slide--agenda">
    <div class="photo" role="img" aria-label="Faded photo of a baseball, glove and bat on grass"></div>
    <header class="agenda-head">
      <h1>AGENDA FOR THE DAY</h1>
      <p>Insert your sub title here</p>
    </header>

    <div class="agenda-item" style="left:67px; top:98px;">
      <svg width="12" height="12" viewBox="0 0 12 12"><circle cx="6" cy="6" r="5.3" fill="#fff" stroke="#c9c9c9" stroke-width="0.8"/><path d="M3.5 1.8c1.4 2.4 1.4 6 0 8.4M8.5 1.8c-1.4 2.4-1.4 6 0 8.4" fill="none" stroke="var(--red)" stroke-width="0.9"/></svg>
      <h2>Introduction</h2>
      <p>What we need is a template (or master) which can be varied by ourselves from case to case.</p>
    </div>
    <div class="agenda-item" style="left:67px; top:154px;">
      <svg width="12" height="12" viewBox="0 0 12 12"><circle cx="6" cy="6" r="5.3" fill="#fff" stroke="#c9c9c9" stroke-width="0.8"/><path d="M3.5 1.8c1.4 2.4 1.4 6 0 8.4M8.5 1.8c-1.4 2.4-1.4 6 0 8.4" fill="none" stroke="var(--red)" stroke-width="0.9"/></svg>
      <h2>Services</h2>
      <p>What we need is a template (or master) which</p>
    </div>
    <div class="agenda-item" style="left:67px; top:200px;">
      <svg width="12" height="12" viewBox="0 0 12 12"><circle cx="6" cy="6" r="5.3" fill="#fff" stroke="#c9c9c9" stroke-width="0.8"/><path d="M3.5 1.8c1.4 2.4 1.4 6 0 8.4M8.5 1.8c-1.4 2.4-1.4 6 0 8.4" fill="none" stroke="var(--red)" stroke-width="0.9"/></svg>
      <h2>Support</h2>
      <p>What we need is a template (or master) which can be varied by ourselves from case to case.</p>
    </div>
    <div class="agenda-item" style="left:322px; top:98px; width:210px;">
      <svg width="12" height="12" viewBox="0 0 12 12"><circle cx="6" cy="6" r="5.3" fill="#fff" stroke="#c9c9c9" stroke-width="0.8"/><path d="M3.5 1.8c1.4 2.4 1.4 6 0 8.4M8.5 1.8c-1.4 2.4-1.4 6 0 8.4" fill="none" stroke="var(--red)" stroke-width="0.9"/></svg>
      <h2>Our&nbsp; Charts</h2>
      <p>What we need is a template (or master)<br>which</p>
    </div>
    <div class="agenda-item" style="left:322px; top:152px; width:210px;">
      <svg width="12" height="12" viewBox="0 0 12 12"><circle cx="6" cy="6" r="5.3" fill="#fff" stroke="#c9c9c9" stroke-width="0.8"/><path d="M3.5 1.8c1.4 2.4 1.4 6 0 8.4M8.5 1.8c-1.4 2.4-1.4 6 0 8.4" fill="none" stroke="var(--red)" stroke-width="0.9"/></svg>
      <h2>Our Team Members</h2>
      <p>What we need is a template (or master) which can be varied by ourselves from case to case.</p>
    </div>
  </section>

</body>
</html>
```